TRIVEL Corp Has New Logo Now Needs New Stationary

We just chose our new logo, and now we need a letterhead and envelope design. I would like both to be used via Microsoft Word so I can print both the letterhead and envelopes myself rather than having to the letterhead and envelopes produced by a printing firm. I has attached the new logo and spec sheet provided by the logo designer.

```html
<!DOCTYPE html>
<html lang="en">
<head>
<meta charset="utf-8">
<title>TRIVEL Corp Stationery</title>
<link href="https://fonts.googleapis.com/css2?family=Arimo:wght@400;700&display=swap" rel="stylesheet">
<style>
  :root {
    --backdrop: #e9e6e2;
    --paper: #ffffff;
    --ink: #333333;
    --ink-soft: #555555;
    --brand-green: #7cc242;
    --brand-teal: #52b79a;
    --brand-blue: #3fa9e0;
    --frame: #555555;
  }
  * { box-sizing: border-box; margin: 0; padding: 0; }
  html, body {
    width: 1200px;
    height: 1002px;
    overflow: hidden;
  }
  body {
    background: var(--backdrop);
    font-family: "Arimo", Arial, sans-serif;
    color: var(--ink);
    position: relative;
  }
  .sheet {
    position: absolute;
    background: var(--paper);
    box-shadow: 0 6px 18px rgba(0,0,0,0.18);
  }
  .brand-band {
    position: absolute;
    left: 0;
    right: 0;
    height: 7px;
    background: linear-gradient(90deg, var(--brand-green), var(--brand-teal), var(--brand-blue));
  }
  .brand-name {
    display: flex;
    align-items: center;
    gap: 10px;
    font-weight: 700;
    color: var(--ink);
    letter-spacing: 0.5px;
    white-space: nowrap;
  }
  .brand-dot {
    width: 22px;
    height: 22px;
    border-radius: 50%;
    background: var(--brand-green);
    flex: none;
  }

  /* Letterhead */
  .letterhead {
    left: 610px;
    top: 110px;
    width: 540px;
    height: 764px;
  }
  .letterhead .brand-name {
    position: absolute;
    top: 52px;
    left: 0;
    right: 0;
    justify-content: center;
    font-size: 26px;
  }
  .letter-title {
    position: absolute;
    top: 118px;
    left: 0;
    right: 0;
    text-align: center;
    font-size: 13px;
    font-weight: 700;
    color: #111;
  }
  .letter-body {
    position: absolute;
    top: 160px;
    left: 52px;
    right: 52px;
    font-size: 10.5px;
    line-height: 1.3;
    color: var(--ink-soft);
    text-indent: 28px;
  }
  .letterhead .brand-band { top: 638px; }
  .letter-footer {
    position: absolute;
    top: 662px;
    left: 0;
    right: 0;
    text-align: center;
    font-size: 11px;
    line-height: 1.35;
    color: var(--ink-soft);
  }
  .letter-footer strong, .envelope-contact strong { color: var(--ink); }

  /* Envelope */
  .envelope {
    left: 50px;
    top: 420px;
    width: 520px;
    height: 260px;
  }
  .envelope .brand-name {
    position: absolute;
    top: 52px;
    left: 40px;
    font-size: 22px;
  }
  .envelope-window {
    position: absolute;
    left: 262px;
    top: 70px;
    width: 232px;
    height: 118px;
    border: 1px solid var(--frame);
    border-radius: 10px;
  }
  .envelope-contact {
    position: absolute;
    top: 120px;
    left: 40px;
    font-size: 10.5px;
    line-height: 1.35;
    color: var(--ink-soft);
    text-align: right;
    width: 178px;
  }
  .envelope .brand-band { top: 214px; }
</style>
</head>
<body>

  <section class="sheet letterhead" aria-label="Letterhead">
    <div class="brand-name"><span class="brand-dot"></span>TRIVEL Corp</div>
    <h1 class="letter-title">Lorem ipsum dolor sit amet, consectetur adipiscing elit.</h1>
    <p class="letter-body">Lorem ipsum dolor sit amet, consectetur adipiscing elit. Phasellus venenatis lorem in euismod posuere. Aenean iaculis malesuada ante sed rhoncus. Nunc facilisis ipsum ipsum, commodo euismod orci commodo sollicitudin. Donec nulla diam, interdum nec consectetur eu, posuere vel lectus. Quisque vel accumsan felis. Quisque posuere odio non erat aliquam, a fringilla sem suscipit. Pellentesque feugiat ornare sapien, id lobortis tortor vehicula et. Donec iaculis cursus lectus quis consectetur. Phasellus gravida nulla non erat fermentum, at euismod nunc ultrices.</p>
    <div class="brand-band"></div>
    <address class="letter-footer" style="font-style:normal">
      48 Harbor Lane, Bridgeton, Maine<br>
      <strong>phone:</strong> 555-018-2740 &nbsp;::&nbsp; <strong>e-mail:</strong> hello@trivelcorp.com<br>
      www.trivelcorp.com
    </address>
  </section>

  <section class="sheet envelope" aria-label="Envelope">
    <div class="brand-name"><span class="brand-dot"></span>TRIVEL Corp</div>
    <address class="envelope-contact" style="font-style:normal">
      48 Harbor Lane, Bridgeton, Maine<br>
      <strong>phone:</strong> 555-018-2740<br>
      <strong>e-mail:</strong> hello@trivelcorp.com<br>
      www.trivelcorp.com
    </address>
    <div class="envelope-window"></div>
    <div class="brand-band"></div>
  </section>

</body>
</html>
```